RZO Design tag

Looking to design a tag for our new hat & glove brand RZO Design. These are winter hats & gloves. Long story short these are lower cost/retail items but I'm trying to convey higher quality goods through a nice tag. I’ve attached a tag of another brand we have to give you a general idea of what I’d be looking for- but again for our new brand RZO Design.
I’m thinking we can do one general design- and then do it in 4 different color schemes: First one mimicking the attachment’s colors for ladies items- so a few different shades of pink. Then 2nd color scheme a darker more masculine color tone for mens or unisex items- maybe blue/dark blue, and then a 3rd color scheme for kids items that is more vibrant/kid like colors. Last one red & green for some Christmas items we do.
A few things:
• Trying to make the tags look classy as possible
• The tag will need to measure 2.25” high x 2” wide. The top little bit would have to be space left blank for a hole punch- just like on the attached sample tag. But again the tags designed would need to be 2.25" tall x 2" wide so not the same shape as the sample tag.
• For item name you can just put “Knit Hat” for the generic tag item name (in place of what says on the same “Chenille Slipper Bootie”). Please try to keep the writing a nice font similar to what is on this tag- again trying to have a classy tag look
• On the bottom center (In place of Made in China) it would just need to say “One Size” in standard font
Hope this helps & thank you
Target Market(s)
People buying winter hats & gloves
Industry/Entity Type
Retail- winter hats & gloves
Look and feel

```html
<!DOCTYPE html>
<html lang="en">
<head>
<meta charset="utf-8">
<title>Knit Hat – Hang Tag</title>
<link rel="stylesheet" href="https://fonts.googleapis.com/css2?family=Kaushan+Script&family=Open+Sans:wght@400;600&display=swap">
<style>
  :root {
    --page-bg: #efe6df;
    --tag-white: #f4f4f6;
    --tag-blue: #2a4fa8;
    --tag-blue-light: #3a62bd;
    --tag-blue-dark: #1f3f8f;
    --pill-blue: #3a6fd0;
    --ink-white: #ffffff;
    --eyelet: #8a3b32;
  }
  * { margin: 0; padding: 0; box-sizing: border-box; }
  html, body {
    width: 1200px;
    height: 800px;
    overflow: hidden;
    background: var(--page-bg);
  }
  .canvas {
    position: relative;
    width: 1200px;
    height: 800px;
    display: flex;
    align-items: center;
    justify-content: center;
  }
  .hang-tag {
    position: relative;
    width: 560px;
    height: 630px;
    background: var(--tag-white);
    box-shadow: 0 6px 22px rgba(80, 50, 30, 0.18);
    overflow: hidden;
  }
  .punch-strip {
    position: absolute;
    top: 0; left: 0; right: 0;
    height: 44px;
    background: var(--tag-white);
  }
  .punch-hole {
    position: absolute;
    top: 10px;
    left: 58px;
    width: 26px;
    height: 26px;
    border-radius: 50%;
    background: var(--page-bg);
    border: 5px solid var(--eyelet);
  }
  .brand-field {
    position: absolute;
    top: 44px; left: 0; right: 0;
    height: 420px;
    background: linear-gradient(150deg, var(--tag-blue-light) 0%, var(--tag-blue) 55%, var(--tag-blue-dark) 100%);
  }
  .item-name {
    position: absolute;
    top: 92px;
    left: 48px;
    font-family: "Kaushan Script", cursive;
    font-weight: 400;
    color: var(--ink-white);
    font-size: 132px;
    line-height: 1.02;
    letter-spacing: 1px;
  }
  .item-name .line-one,
  .item-name .line-two {
    display: block;
  }
  .item-name .line-two {
    padding-left: 190px;
  }
  .size-band {
    position: absolute;
    left: 0; right: 0; bottom: 0;
    height: 166px;
    background: var(--tag-white);
  }
  .size-pill {
    position: absolute;
    top: 26px;
    right: 40px;
    padding: 6px 20px 7px;
    border-radius: 999px;
    background: var(--pill-blue);
    color: var(--ink-white);
    font-family: "Open Sans", sans-serif;
    font-size: 22px;
    font-weight: 400;
    white-space: nowrap;
  }
</style>
</head>
<body>
  <main class="canvas">
    <article class="hang-tag">
      <div class="punch-strip"><span class="punch-hole"></span></div>
      <div class="brand-field" role="img" aria-label="Deep blue field with a faint repeating brand-name pattern"></div>
      <h1 class="item-name"><span class="line-one">Knit</span><span class="line-two">Hat</span></h1>
      <div class="size-band">
        <span class="size-pill">One Size</span>
      </div>
    </article>
  </main>
</body>
</html>
```